1912 Zur Glutpfanne Website
Zielgruppe
Wir betreiben ein Hamburger-Restaurant. Alle Zutaten kommen wenn möglich, aus der Region. Wir benutzen keine Farb- und Konservierungsstoffe. Unser Fleisch ist ein frisches Bio-Rinderhack. Das Brot backen wir selber und die Saucen sind nach eigener Rezeptur hausgemacht. Der Käse wird in einem Familienbetrieb frisch für uns hergestellt. Jeder Gast kann sich seinen Burger frisch nach seinen Wünschen zusammenstellen und bei der Zubereitung zuschauen. Essen mit Herkunft aus Tradition!
Aufgabenstellung
Ansprechendes Design, welches unsere Philosophie und die Liebe zum Burger widerspiegelt. Frische Zutaten in wechselnden Slide-Shows, Wertschätzung der Rohprodukte und den Genuss beim Essen.

```html
<!DOCTYPE html>
<html lang="de">
<head>
<meta charset="utf-8">
<title>1912 Zur Glutpfanne</title>
<link href="https://fonts.googleapis.com/css2?family=Cutive&family=Open+Sans:wght@700&display=swap" rel="stylesheet">
<style>
  :root {
    --brown-dark: #4a1e0f;
    --brown: #4f2114;
    --beige: #d3c8bc;
    --text-grey: #5a4e48;
    --white: #ffffff;
    --faint: #e8e3de;
    --cream: #efe9df;
  }
  * { margin: 0; padding: 0; box-sizing: border-box; }
  html, body { width: 711px; height: 1200px; overflow: hidden; background: var(--white); }
  body { font-family: "Cutive", "Courier New", serif; position: relative; }

  .header { position: absolute; left: 0; top: 0; width: 711px; height: 288px; }
  .header__side {
    position: absolute; left: 0; top: 0; width: 178px; height: 288px;
    background: linear-gradient(160deg, #f3eee6 0%, var(--cream) 60%, #e3ddd0 100%);
  }
  .brand {
    position: absolute; left: 14px; top: 40px; width: 156px;
    display: flex; align-items: center; gap: 8px;
  }
  .brand__dot { width: 14px; height: 14px; border-radius: 50%; background: var(--brown); flex: none; }
  .brand__name { color: var(--brown); font-size: 18px; line-height: 23px; }
  .header__photo {
    position: absolute; left: 178px; top: 0; width: 533px; height: 288px;
    background: radial-gradient(ellipse at 55% 45%, #6b3320 0%, #8a5a3a 35%, #c59a6c 60%, #d8b890 100%);
  }

  .nav { position: absolute; left: 0; top: 288px; width: 711px; height: 29px; background: var(--brown-dark); }
  .nav__item { position: absolute; top: 7px; color: var(--white); font-size: 12.5px; text-transform: uppercase; }

  .intro { position: absolute; left: 0; top: 317px; width: 711px; height: 197px; }
  .intro__side { position: absolute; left: 0; top: 0; width: 178px; height: 197px; background: var(--white); }
  .intro__deco { position: absolute; left: 33px; top: 72px; width: 145px; height: 84px; background: var(--faint); }
  .intro__panel { position: absolute; left: 178px; top: 0; width: 533px; height: 197px; background: var(--beige); }
  .intro__title { position: absolute; left: 60px; top: 26px; color: var(--brown); font-size: 31px; font-weight: 400; white-space: nowrap; }
  .intro__text { position: absolute; left: 60px; top: 72px; width: 450px; color: var(--text-grey); font-size: 15.5px; line-height: 21.7px; }

  .grill {
    position: absolute; left: 0; top: 514px; width: 711px; height: 197px;
    background: radial-gradient(ellipse at 40% 55%, #e46a14 0%, #a33a0c 30%, #3a1a0c 60%, #0f0b09 100%);
  }

  .origin { position: absolute; left: 0; top: 711px; width: 711px; height: 393px; }
  .origin__side { position: absolute; left: 0; top: 0; width: 178px; height: 393px; background: var(--white); }
  .origin__deco { position: absolute; left: 0; top: 149px; width: 178px; height: 202px; background: var(--faint); }
  .origin__panel { position: absolute; left: 178px; top: 0; width: 533px; height: 393px; background: var(--beige); }
  .origin__path { position: absolute; left: 0; top: 0; }
  .step__marker { position: absolute; width: 36px; height: 36px; border-radius: 50%; background: var(--brown); }
  .step__text { position: absolute; color: var(--text-grey); font-size: 12.5px; line-height: 16.7px; white-space: nowrap; }

  .footer { position: absolute; left: 0; top: 1104px; width: 711px; height: 96px; background: var(--brown-dark); }
  .footer__col { position: absolute; top: 26px; color: var(--white); }
  .footer__title { font-size: 9px; text-transform: uppercase; margin-bottom: 2px; }
  .footer__link { font-family: "Open Sans", Arial, sans-serif; font-weight: 700; font-size: 7.5px; line-height: 14px; }
</style>
</head>
<body>
  <header class="header">
    <div class="header__side">
      <div class="brand">
        <span class="brand__dot"></span>
        <span class="brand__name">1912 Zur Glutpfanne</span>
      </div>
    </div>
    <div class="header__photo" role="img" aria-label="Nahaufnahme eines Burgers mit Vollkornbrötchen, Patty, Salat und heller Sauce"></div>
  </header>

  <nav class="nav">
    <span class="nav__item" style="left:239px">Menüpunkt</span>
    <span class="nav__item" style="left:393px">Weiterer</span>
    <span class="nav__item" style="left:525px">Ein Punkt</span>
  </nav>

  <section class="intro">
    <div class="intro__side"><div class="intro__deco" role="img" aria-label="Dezente Hintergrundillustration eines Pattys"></div></div>
    <div class="intro__panel">
      <h1 class="intro__title">Hamburgefonts</h1>
      <p class="intro__text">Dies ist ein Typoblindtext. An ihm kann man sehen, ob alle Buchstaben da sind und wie sie aussehen. Manchmal benutzt man Worte wie Hamburgefonts, Rafgenduks oder Handgloves, um Schriften zu testen.</p>
    </div>
  </section>

  <div class="grill" role="img" aria-label="Patties auf einem Grillrost über offenen Flammen mit Grillwender"></div>

  <section class="origin">
    <div class="origin__side"><div class="origin__deco" role="img" aria-label="Dezente Hintergrundillustration eines Brotlaibs"></div></div>
    <div class="origin__panel"></div>
    <svg class="origin__path" width="711" height="393" viewBox="0 0 711 393">
      <path d="M270 70 C290 100 350 110 422 116 M460 128 C500 140 540 160 535 185 C530 215 500 235 462 248 M420 256 C370 250 320 230 278 196 M244 196 C225 230 228 280 250 310"
            fill="none" stroke="#5a4e48" stroke-width="4" stroke-dasharray="9 6"/>
    </svg>

    <span class="step__marker" style="left:241px;top:34px" role="img" aria-label="Illustration: Tomate"></span>
    <p class="step__text" style="left:294px;top:41px">Alle Zutaten kommen<br>frisch aus der Region.</p>

    <span class="step__marker" style="left:424px;top:102px" role="img" aria-label="Illustration: Patty"></span>
    <p class="step__text" style="left:495px;top:100px">Unser Fleisch ist ein<br>frisches Bio-Rinderhack.</p>

    <span class="step__marker" style="left:244px;top:163px" role="img" aria-label="Illustration: Brot"></span>
    <p class="step__text" style="left:298px;top:168px">Das Brot backen wir selber<br>aus bestem Getreide.</p>

    <span class="step__marker" style="left:419px;top:232px" role="img" aria-label="Illustration: Saucenschale"></span>
    <p class="step__text" style="left:464px;top:253px">Die Saucen sind nach eigener<br>Rezeptur hausgemacht.</p>

    <span class="step__marker" style="left:244px;top:308px" role="img" aria-label="Illustration: Käsestück"></span>
    <p class="step__text" style="left:298px;top:318px">Der Käse wird in einem Familien-<br>betrieb frisch für uns hergestellt.</p>
  </section>

  <footer class="footer">
    <div class="footer__col" style="left:237px">
      <p class="footer__title">Platzhalter</p>
      <p class="footer__link">Das ist ein Blindtext</p>
      <p class="footer__link">Das auch</p>
      <p class="footer__link">Und das natürlich</p>
    </div>
    <div class="footer__col" style="left:370px">
      <p class="footer__title">Platz</p>
      <p class="footer__link">Das ist ein Blindtext</p>
      <p class="footer__link">Das auch</p>
      <p class="footer__link">Und das auch</p>
    </div>
    <div class="footer__col" style="left:501px">
      <p class="footer__title">Platzhalter</p>
      <p class="footer__link">Das ist einer</p>
      <p class="footer__link">Das auch</p>
      <p class="footer__link">Und das natürlich</p>
    </div>
  </footer>
</body>
</html>
```